Personal training and nutrition business needs business card design

We need a business card that outlays our services and invites potential customers to join our team and take the first step to a healthier and more enjoyable life. We cater for any level of fitness and specialize in weight loss and conditioning, strength training, muscle gain and strength endurance. Whether you are just starting off or need some help getting to the next level of your journey we are here to get the job done.
We specialize in one on one or one on two personal training sessions and each program will be custom made to suit individual fitness goals of our clients

```html
<!DOCTYPE html>
<html lang="en">
<head>
<meta charset="utf-8">
<title>Stride &amp; Sweat — Business Card</title>
<link rel="stylesheet" href="https://fonts.googleapis.com/css2?family=Saira+Condensed:wght@800&family=Oswald:wght@500&family=Arimo:wght@400;700&display=swap">
<style>
  :root {
    --stage: #2a2a2c;
    --ink: #0a0a0a;
    --paper: #ffffff;
    --purple: #7b4fb0;
    --purple-dark: #7a4db0;
    --purple-light: #9c60b6;
    --purple-text: #6a3fa6;
    --tag: #8e55b8;
    --grey: #5a5a5a;
    --body-text: #222222;
  }
  * { box-sizing: border-box; margin: 0; padding: 0; }
  html, body { width: 1200px; height: 900px; overflow: hidden; }
  body { background: var(--stage); position: relative; }

  .card {
    position: absolute;
    left: 280px;
    width: 640px;
    height: 366px;
    overflow: hidden;
    box-shadow: 0 10px 30px rgba(0,0,0,.45);
  }
  .card--front { top: 70px; background: var(--ink); }
  .card--back  { top: 464px; background: var(--paper); }

  .side-band {
    position: absolute;
    top: 0;
    right: 0;
    height: 100%;
    background: linear-gradient(200deg, var(--purple-light), var(--purple-dark));
  }
  .card--front .side-band { width: 190px; }
  .card--back .side-band  { width: 200px; }

  .brand { position: absolute; }
  .card--front .brand { left: 120px; top: 96px; }
  .card--back .brand  { left: 40px; top: 40px; }

  .brand__mark {
    width: 54px; height: 54px;
    background: var(--purple);
    border-radius: 6px;
    margin-bottom: 12px;
    margin-left: 40px;
  }
  .brand__name {
    font-family: "Saira Condensed", sans-serif;
    font-weight: 800;
    font-size: 50px;
    line-height: .9;
    letter-spacing: 1px;
    text-transform: uppercase;
  }
  .card--front .brand__name { color: var(--paper); }
  .card--back .brand__name  { color: var(--ink); font-size: 54px; }

  .brand__tagline {
    font-family: "Oswald", sans-serif;
    font-weight: 500;
    font-size: 11px;
    letter-spacing: 1.2px;
    text-transform: uppercase;
    color: var(--tag);
    margin-top: 8px;
  }

  .person { position: absolute; left: 58px; top: 190px; }
  .person__name {
    font-family: "Arimo", sans-serif;
    font-weight: 700;
    font-size: 20px;
    color: var(--purple-text);
  }
  .person__role {
    font-family: "Arimo", sans-serif;
    font-size: 12px;
    color: var(--grey);
    margin-top: 2px;
  }

  .contact {
    position: absolute; left: 58px; top: 250px;
    list-style: none;
    font-family: "Arimo", sans-serif;
    font-size: 13px;
    color: var(--body-text);
  }
  .contact__item { display: flex; align-items: flex-start; gap: 12px; line-height: 1.25; }
  .contact__item--address { margin-bottom: 12px; }
  .contact__icon { width: 14px; height: 14px; flex: none; margin-top: 1px; fill: var(--purple); }
</style>
</head>
<body>

  <section class="card card--front" aria-label="Card front">
    <div class="side-band" role="img" aria-label="Purple side band with brand decoration"></div>
    <div class="brand">
      <div class="brand__mark"></div>
      <p class="brand__name">Stride<br>&amp; Sweat</p>
      <p class="brand__tagline">Personal training. Nutrition. Motivation</p>
    </div>
  </section>

  <section class="card card--back" aria-label="Card back">
    <div class="side-band" role="img" aria-label="Purple side band with brand decoration"></div>

    <div class="brand">
      <p class="brand__name">Stride<br>&amp; Sweat</p>
      <p class="brand__tagline">Personal training. Nutrition. Motivation</p>
    </div>

    <div class="person">
      <p class="person__name">Marco Delvane</p>
      <p class="person__role">Director</p>
    </div>

    <ul class="contact">
      <li class="contact__item contact__item--address">
        <svg class="contact__icon" viewBox="0 0 24 24" aria-hidden="true"><path d="M12 2a7 7 0 0 0-7 7c0 5 7 13 7 13s7-8 7-13a7 7 0 0 0-7-7zm0 9.5A2.5 2.5 0 1 1 12 6.5a2.5 2.5 0 0 1 0 5z"/></svg>
        <span>48 Harbor Point Lane,<br>Clearwater, Florida 33755</span>
      </li>
      <li class="contact__item">
        <svg class="contact__icon" viewBox="0 0 24 24" aria-hidden="true"><path d="M6.6 10.8a15 15 0 0 0 6.6 6.6l2.2-2.2a1 1 0 0 1 1-.25 11 11 0 0 0 3.6.57 1 1 0 0 1 1 1V20a1 1 0 0 1-1 1A17 17 0 0 1 3 4a1 1 0 0 1 1-1h3.5a1 1 0 0 1 1 1c0 1.25.2 2.45.57 3.57a1 1 0 0 1-.25 1z"/></svg>
        <span>012 555 0147</span>
      </li>
      <li class="contact__item">
        <svg class="contact__icon" viewBox="0 0 24 24" aria-hidden="true"><path d="M2 5h20v14H2z M2 5l10 8 10-8" fill="none" stroke="var(--purple)" stroke-width="2"/></svg>
        <span>hello@strideandsweat.com</span>
      </li>
      <li class="contact__item">
        <svg class="contact__icon" viewBox="0 0 24 24" aria-hidden="true"><circle cx="12" cy="12" r="9" fill="none" stroke="var(--purple)" stroke-width="2"/><path d="M3 12h18M12 3c3 3 3 15 0 18M12 3c-3 3-3 15 0 18" fill="none" stroke="var(--purple)" stroke-width="1.6"/></svg>
        <span>www.strideandsweat.com</span>
      </li>
    </ul>
  </section>

</body>
</html>
```